Long term Care Provider Conference

Banner for LTC providers to know that they can rely on us to deliver high value, cost efficient, professional back office support to streamline operations, improve and maintain compliance with administrative and or nursing solutions for their agency.

Want to update the wording

```html
<!DOCTYPE html>
<html lang="en">
<head>
<meta charset="utf-8">
<title>Meridia Solutions – LTC Provider Conference Banner</title>
<link href="https://fonts.googleapis.com/css2?family=Poppins:wght@300;400;500;600;700&display=swap" rel="stylesheet">
<style>
  :root{
    --page:#ececec;
    --white:#ffffff;
    --ink:#1f2a2e;
    --taupe:#b1a193;
    --teal:#3f6b74;
    --band-dark:#435f68;
    --band-light:#5e8c97;
    --url-bar:#3b565f;
    --photo-a:#c9d3d6;
    --photo-b:#8fa3aa;
  }
  *{box-sizing:border-box;margin:0;padding:0}
  html,body{width:1116px;height:1200px;overflow:hidden;background:var(--page)}
  body{font-family:'Poppins',sans-serif;position:relative}
  .banner{
    position:absolute;left:17px;top:10px;width:1250px;height:1364px;
    transform:scale(0.865);transform-origin:0 0;
    background:var(--white);overflow:hidden;
  }
  .hero-photo{
    position:absolute;right:0;top:0;width:640px;height:690px;
    background:linear-gradient(160deg,var(--photo-a),var(--photo-b));
    -webkit-mask-image:linear-gradient(90deg,transparent 0,#000 35%),linear-gradient(0deg,transparent 0,#000 20%);
    -webkit-mask-composite:source-in;mask-composite:intersect;
  }
  .brand{position:absolute;left:85px;top:88px;display:flex;align-items:center;gap:20px}
  .brand-dot{width:80px;height:80px;border-radius:50%;background:var(--teal)}
  .brand-name{font-weight:700;font-size:48px;color:var(--ink);letter-spacing:-1px}
  .headline{position:absolute;left:83px;top:210px;font-size:63px;line-height:68px;font-weight:700;letter-spacing:-0.5px;white-space:nowrap}
  .headline .lead{color:var(--taupe)}
  .headline .tail{color:var(--teal)}
  .headline .light{font-weight:400}
  .rule{position:absolute;left:85px;top:502px;width:575px;height:2px;background:linear-gradient(90deg,var(--teal),rgba(63,107,116,0))}
  .intro{position:absolute;left:85px;top:522px;width:600px;font-size:23px;line-height:30px;color:var(--ink)}
  .intro b{font-weight:600}
  .band{position:absolute;left:0;top:765px;width:1250px;height:600px;background:linear-gradient(100deg,var(--band-dark) 55%,var(--band-light))}
  .services{position:absolute;left:85px;top:695px;display:flex;gap:33px}
  .service{width:245px;text-align:center}
  .service-photo{height:160px;border:8px solid var(--white);border-radius:8px;box-shadow:0 4px 10px rgba(0,0,0,.25);background:linear-gradient(150deg,var(--photo-a),var(--photo-b))}
  .service-label{margin-top:18px;color:var(--white);font-weight:600;font-size:25px;line-height:33px;text-transform:uppercase}
  .facts{position:absolute;left:80px;top:997px;display:flex;align-items:center}
  .badge-circle{width:82px;height:82px;border-radius:50%;background:#8fa0a5;border:4px solid #b7c3c6;display:flex;align-items:center;justify-content:center}
  .experience{margin-left:18px;color:#e8eef0;font-size:26px;line-height:32px;font-weight:300}
  .experience b{font-weight:600}
  .divider{width:1px;height:70px;background:rgba(255,255,255,.25);margin:0 44px}
  .cert{width:152px;height:64px;display:flex;align-items:center;gap:10px}
  .cert-bar{flex:1;height:40px;border-radius:4px;background:rgba(255,255,255,.85)}
  .url{position:absolute;left:790px;top:1013px;width:460px;height:52px;background:var(--url-bar);color:#dfe7e9;font-size:38px;line-height:52px;padding-left:15px;font-weight:300}
  .url b{font-weight:700}
</style>
</head>
<body>
  <main class="banner">
    <div class="hero-photo" role="img" aria-label="Photo of back office staff with headsets working at computers in a bright office"></div>

    <div class="brand">
      <span class="brand-dot"></span>
      <span class="brand-name">Meridia Solutions</span>
    </div>

    <h1 class="headline">
      <span class="lead">Streamlining<br>Long Term Care</span><br>
      <span class="tail"><span class="light">with </span>Professional<br>Back Office Support</span>
    </h1>
    <div class="rule"></div>
    <p class="intro">LTC providers can rely on us for <b>high value, cost efficient</b> back office support that <b>streamlines operations</b> and keeps your agency <b>compliant</b> with administrative and nursing solutions.</p>

    <div class="band"></div>

    <section class="services">
      <div class="service"><div class="service-photo" role="img" aria-label="Nurse in scrubs working at a laptop"></div><p class="service-label">Registered<br>Nurse</p></div>
      <div class="service"><div class="service-photo" role="img" aria-label="Staff with headsets in an office meeting"></div><p class="service-label">Human<br>Resources</p></div>
      <div class="service"><div class="service-photo" role="img" aria-label="Gloved hand writing on a billing form"></div><p class="service-label">Medical<br>Billing</p></div>
      <div class="service"><div class="service-photo" role="img" aria-label="Support agent with headset and team in background"></div><p class="service-label">Administrative<br>Support</p></div>
    </section>

    <section class="facts">
      <div class="badge-circle">
        <svg width="44" height="40" viewBox="0 0 44 40" fill="none" stroke="#fff" stroke-width="2.5"><circle cx="12" cy="14" r="5"/><circle cx="32" cy="14" r="5"/><circle cx="22" cy="10" r="5"/><path d="M3 34c0-7 4-11 9-11s9 4 9 11M23 34c0-7 4-11 9-11s9 4 9 11"/></svg>
      </div>
      <p class="experience">More than <b>20 years</b><br>of business expertise</p>
      <span class="divider"></span>
      <div class="cert">
        <svg width="52" height="60" viewBox="0 0 52 60"><path d="M26 2 L50 10 V30 C50 46 38 54 26 58 C14 54 2 46 2 30 V10 Z" fill="#fff"/></svg>
        <span class="cert-bar"></span>
      </div>
    </section>

    <p class="url">www.<b>meridia-va</b>.com</p>
  </main>
</body>
</html>
```